Business Card Design for Retail Product Line

We need a two-sided, full-color business card for a new oral care product line. The feel of the card should invoke emotions of happiness and health. It should be bright, cheerful and modern in appearance. The card should be mostly matte finish, but with elements of spot-gloss and/or raised/embossed features (print, logo, tag lines, etc.).

Target Market(s)

People who are into whole-body health, eat well and understand the importance of nutrition.

Industry/Entity Type

Health And Wellness

Contact Information for Business Card

The logo, color scheme and tag-lines have all been developed and artwork is attached. Card is to be standard-sized and should use a mix of clean, sans-serif fonts; the main font (DIN) is attached as well. The card will be used for 3 individuals and should include placeholders for:
1. Name
2. Title (for example, "CEO")
3. Business address
4. Phone number
5. Website
6. Email address

Font styles to use
Sans Serif
Other font styles liked:
• DIN font

Colors
faa54b
000000
5c5c5c
a2ce44

Requirements
Must have
• 2 sides
• Full color orange on one side
• Image of DNA leaves
• Tag line "Glow from the Root Upward", on single side with orange background
• Company Logo (Plome) on same side as text (name, phone, address, etc.)
• Name, Title, Business Address, Phone Number, Website, Email address
• UPDATE: "Brisk Marrow", not "Brisk M Arrow"
Should not have
• Calligraphy
• Dark colors
• UPDATE!! Do not include "Turmeric infused toothpaste" on the business card
• UPDATE #2!! Do not include "Brisk Marrow" on the business card

```html
<!DOCTYPE html>
<html lang="en">
<head>
<meta charset="utf-8">
<title>Plome Business Card</title>
<link rel="stylesheet" href="https://fonts.googleapis.com/css2?family=Open+Sans:wght@400;600;700&family=Barlow+Semi+Condensed:wght@600;700&display=swap">
<style>
  :root {
    --stage: #ecebe8;
    --lime: #b9d534;
    --lime-light: #c4dc3e;
    --leaf-dark: #0f9a47;
    --leaf-mid: #4cb848;
    --helix-grey: #a9a9a9;
    --ink: #111111;
    --ink-soft: #222222;
    --orange-top: #efc43b;
    --orange-bottom: #e79b2b;
    --white: #ffffff;
  }
  * { box-sizing: border-box; margin: 0; padding: 0; }
  html, body { width: 1200px; height: 900px; overflow: hidden; }
  body {
    background: var(--stage);
    position: relative;
    font-family: "Open Sans", Arial, sans-serif;
  }
  .card {
    position: absolute;
    overflow: hidden;
    box-shadow: 0 6px 18px rgba(0,0,0,0.18);
  }
  /* Front side */
  .card-front {
    left: 238px; top: 60px;
    width: 555px; height: 345px;
    background: var(--lime);
    color: var(--ink);
  }
  .dna-leaf-art {
    position: absolute;
    right: 0; top: 0;
    width: 265px; height: 345px;
  }
  .brand-name {
    position: absolute;
    left: 38px; top: 34px;
    font-weight: 700;
    font-size: 62px;
    line-height: 1;
    letter-spacing: -1px;
    color: var(--ink);
  }
  .person {
    position: absolute;
    left: 40px; top: 160px;
  }
  .person-name {
    font-weight: 700;
    font-size: 17.5px;
    line-height: 22px;
    color: var(--ink-soft);
  }
  .person-title {
    font-size: 14.5px;
    line-height: 18px;
    color: var(--ink-soft);
  }
  .address {
    position: absolute;
    left: 40px; top: 216px;
    font-size: 14.5px;
    line-height: 20px;
    color: var(--ink-soft);
    font-style: normal;
  }
  .contact-list {
    position: absolute;
    left: 40px; top: 262px;
    list-style: none;
    font-size: 14.5px;
    line-height: 20px;
    color: var(--ink-soft);
  }
  .contact-list li { display: flex; align-items: center; gap: 8px; }
  .contact-icon { width: 11px; height: 11px; flex: none; }

  /* Back side */
  .card-back {
    left: 459px; top: 518px;
    width: 559px; height: 342px;
    background: linear-gradient(180deg, var(--orange-top) 0%, var(--orange-top) 40%, var(--orange-bottom) 100%);
    color: var(--white);
  }
  .brand-name-reverse {
    position: absolute;
    left: 0; right: 0; top: 68px;
    text-align: center;
    font-family: "Open Sans", Arial, sans-serif;
    font-weight: 700;
    font-size: 72px;
    line-height: 1;
    letter-spacing: -1px;
    color: var(--white);
  }
  .tagline {
    position: absolute;
    left: 214px; top: 218px;
    font-family: "Barlow Semi Condensed", "Arial Narrow", sans-serif;
    color: var(--white);
  }
  .tagline-lead {
    display: block;
    font-weight: 700;
    font-size: 42px;
    line-height: 36px;
  }
  .tagline-rest {
    display: block;
    font-weight: 700;
    font-size: 21px;
    line-height: 21px;
    text-transform: uppercase;
  }
  .tagline-rest sup { font-size: 12px; vertical-align: 6px; }
</style>
</head>
<body>

<section class="card card-front" aria-label="Business card front">
  <svg class="dna-leaf-art" viewBox="0 0 265 345" role="img" aria-label="Illustration of a green and grey DNA helix ending in two green leaves">
    <defs>
      <linearGradient id="leafField" x1="0" y1="0" x2="1" y2="1">
        <stop offset="0" stop-color="#4cb848"/>
        <stop offset="1" stop-color="#0f9a47"/>
      </linearGradient>
    </defs>
    <path d="M110 0 H265 V345 H0 C40 300 70 240 100 180 C120 120 95 60 110 0 Z" fill="url(#leafField)"/>
  </svg>

  <div class="brand-name">Plome</div>

  <div class="person">
    <p class="person-name">Daniel Hartwell</p>
    <p class="person-title">Managing Director</p>
  </div>

  <address class="address">
    48 Orchard Lane, Suite 2<br>
    Greenfield, 204518.
  </address>

  <ul class="contact-list">
    <li>
      <svg class="contact-icon" viewBox="0 0 12 12" aria-hidden="true"><path d="M2.3 0.6 L4.2 2.8 L3.2 4.2 C3.9 5.7 5.2 7.2 7.8 8.8 L9.2 7.8 L11.4 9.7 L10.2 11.4 C5.5 11 1 6.5 0.6 1.8 Z" fill="#111"/></svg>
      <span>044-555 018 372</span>
    </li>
    <li>
      <svg class="contact-icon" viewBox="0 0 12 12" aria-hidden="true"><rect x="1" y="2.5" width="10" height="7" fill="#111"/><path d="M1.5 3 L6 6.5 L10.5 3" fill="none" stroke="#c4dc3e" stroke-width="1"/></svg>
      <span>hello@plomecare.com</span>
    </li>
    <li>
      <svg class="contact-icon" viewBox="0 0 12 12" aria-hidden="true"><circle cx="6" cy="6" r="5.5" fill="#111"/><path d="M3 3.5 C5 4 4.5 6 6 6.5 C7 7 6.5 9 5.5 10.5 M8 2 C7.5 3.5 9 4.5 10.5 4.5" fill="none" stroke="#c4dc3e" stroke-width="1"/></svg>
      <span>www.plomecare.com</span>
    </li>
  </ul>
</section>

<section class="card card-back" aria-label="Business card back">
  <div class="brand-name-reverse">Plome</div>
  <p class="tagline">
    <span class="tagline-lead">glow</span>
    <span class="tagline-rest">from the<br>root upward <sup>™</sup></span>
  </p>
</section>

</body>
</html>
```